the ridgewell craft premier branch

design a DL A4 tri fold brochure to reflect our creative landscape business
my web site www.theridgewellcraft.com.au
has all the information needed
i will also be updating the website to be more updated and creative design

```html
<!DOCTYPE html>
<html lang="en">
<head>
<meta charset="utf-8">
<title>The Ridgewell Craft – Tri-fold Brochure</title>
<link href="https://fonts.googleapis.com/css2?family=Montserrat:wght@400;500;600;700;800&display=swap" rel="stylesheet">
<style>
:root{
  --backdrop:#4b4b4d;
  --paper:#f4f4f4;
  --ink:#1d1d1f;
  --ink-soft:#3a3a3c;
  --orange:#f0901d;
  --blue:#29b7e6;
  --green:#3aa935;
  --dark-band:#3b3c3e;
  --white:#ffffff;
}
*{margin:0;padding:0;box-sizing:border-box}
html,body{width:1200px;height:800px;overflow:hidden;background:var(--backdrop);font-family:"Montserrat",Arial,sans-serif}
.brochure{position:absolute;left:60px;top:18px;width:1080px;height:764px;background:var(--paper);overflow:hidden;box-shadow:0 10px 30px rgba(0,0,0,.35)}
.brochure-shapes{position:absolute;inset:0}
.panel{position:absolute;top:0;width:360px;height:764px}
.panel--about{left:0}
.panel--contact{left:360px}
.panel--cover{left:720px}

.band-text{position:absolute;color:var(--white);font-weight:600;font-size:13px;line-height:1.35}
.band-quote{left:400px;top:70px;width:250px;padding-left:14px;border-left:4px solid var(--blue)}
.band-intro{left:400px;top:220px;width:260px}
.band-intro .lead{color:var(--orange);font-weight:700;display:inline-block;padding-bottom:5px;border-bottom:2px solid var(--orange);margin-bottom:6px;width:100%}
.band-intro .accent{color:var(--blue);font-weight:700}

.about-title{position:absolute;left:36px;top:262px;font-size:26px;font-weight:800;color:var(--ink)}
.about-body{position:absolute;left:36px;top:310px;width:290px;font-size:11.5px;line-height:1.5;color:var(--ink-soft)}
.about-body p{margin-bottom:12px}

.brand{display:flex;align-items:center;gap:10px;font-weight:700;color:var(--ink)}
.brand-dot{width:22px;height:22px;border-radius:50%;background:var(--orange);flex:none}
.brand-name{font-size:19px;line-height:1.15}

.contact{position:absolute;left:40px;top:420px;width:290px}
.contact .brand{margin-bottom:26px}
.contact-name{font-size:26px;font-weight:700;color:var(--ink);margin-bottom:10px}
.contact-name .first{color:var(--orange)}
.contact-phone{font-size:16px;font-weight:700;color:var(--green);margin-bottom:8px}
.contact-line{font-size:12.5px;font-weight:500;color:var(--ink);line-height:1.6}

.cover-title{position:absolute;left:40px;top:470px;width:290px}
.cover-title .creative{display:block;text-align:right;padding-right:20px;font-size:30px;font-weight:800;color:var(--blue);line-height:1}
.cover-title .landscape{display:block;font-size:54px;font-weight:800;color:var(--orange);line-height:.95;letter-spacing:-1px}
.cover-title .sub{display:block;font-size:16px;font-weight:600;color:var(--ink-soft);margin-top:4px}
.cover-brand{position:absolute;left:52px;top:660px;width:270px}
</style>
</head>
<body>
<main class="brochure">
  <svg class="brochure-shapes" viewBox="0 0 1080 764" width="1080" height="764" aria-hidden="false">
    <defs>
      <linearGradient id="gardenDark" x1="0" y1="0" x2="1" y2="1">
        <stop offset="0" stop-color="#5b6a58"/>
        <stop offset=".5" stop-color="#3c4040"/>
        <stop offset="1" stop-color="#2d2e30"/>
      </linearGradient>
      <linearGradient id="gardenLight" x1="0" y1="0" x2="0" y2="1">
        <stop offset="0" stop-color="#8fb87a"/>
        <stop offset=".55" stop-color="#a9aba5"/>
        <stop offset="1" stop-color="#6b5748"/>
      </linearGradient>
    </defs>
    <rect width="1080" height="764" fill="#f4f4f4"/>
    <rect x="360" width="360" height="764" fill="#f7f7f7"/>
    <g role="img" aria-label="Photo of a landscaped courtyard garden under a dark overlay">
      <path d="M0 0 H720 V220 C650 330 470 360 320 300 C210 255 90 215 0 205 Z" fill="url(#gardenDark)"/>
      <path d="M0 0 H720 V220 C650 330 470 360 320 300 C210 255 90 215 0 205 Z" fill="#222" opacity=".35"/>
    </g>
    <path d="M40 -40 L150 -40 L205 55 L150 150 L40 150 Z" fill="#29b7e6" stroke="#ffffff" stroke-width="12" stroke-linejoin="round"/>
    <path d="M765 70 L835 10 H1080 V320 L990 415 H850 L760 330 Z" fill="url(#gardenLight)" stroke="#ffffff" stroke-width="16" stroke-linejoin="round" role="img" aria-label="Photo of a modern paved garden with outdoor seating and greenery"/>
    <rect x="985" y="360" width="92" height="92" rx="18" transform="rotate(45 1031 406)" fill="#f0901d" stroke="#ffffff" stroke-width="8"/>
    <line x1="360" y1="0" x2="360" y2="764" stroke="#e2e2e2"/>
    <line x1="720" y1="0" x2="720" y2="764" stroke="#e2e2e2"/>
  </svg>

  <section class="panel panel--about">
    <h2 class="about-title">About Us</h2>
    <div class="about-body">
      <p>The Ridgewell Craft (TRC), formerly Dale Harrow Landscapes, is a professional construction service that takes pride in high-end outdoor landscapes across Victoria.</p>
      <p>As part of The Ridgewell Craft, our team offers a full service, following every project from concept through installation and maintenance, so each creation becomes part of the home.</p>
      <p>Our business has developed a reputation for positive customer relationships, quality designs and tailored styles. With Dale Harrow's team, you work alongside capable and experienced specialists.</p>
      <p>We endeavour to uphold our standard of excellence in the residential markets, including small gardens through to acreage of every size.</p>
    </div>
  </section>

  <p class="band-text band-quote">Our Clients Will Experience Honesty, Integrity, And Professionalism Throughout The Project Which Allows Them To Embrace Their Outdoor Living After Completion.</p>
  <p class="band-text band-intro"><span class="lead">The Ridgewell Craft</span><br>Is A Full-service Landscaping &amp; Construction Team That Relish <span class="accent">The Journey To Deliver</span> High-end And Bespoke Outdoor Designs.</p>

  <section class="panel panel--contact">
    <div class="contact">
      <div class="brand"><span class="brand-dot"></span><span class="brand-name">The Ridgewell Craft Premier Branch</span></div>
      <p class="contact-name"><span class="first">Dale</span> Harrow</p>
      <p class="contact-phone">Tel: 0400 318 642</p>
      <p class="contact-line">PO BOX 208 Ashvale VIC 3999</p>
      <p class="contact-line">Email: info@theridgewellcraft.com.au</p>
      <p class="contact-line">Web: www.theridgewellcraft.com.au</p>
    </div>
  </section>

  <section class="panel panel--cover">
    <h1 class="cover-title">
      <span class="creative">Creative</span>
      <span class="landscape">Landscape</span>
      <span class="sub">Design &amp; Construction</span>
    </h1>
    <div class="brand cover-brand"><span class="brand-dot"></span><span class="brand-name">The Ridgewell Craft Premier Branch</span></div>
  </section>
</main>
</body>
</html>
```